Frozen Yoghurt Flyer Design Project

Hello, we are looking for a flyer design for a frozen yoghurt shop competition called 'Top Zelmi' (Zelmi is the shop name). This competition rule is simply post your yoghurt creation on Zelmi Chatterly and tag #topzelmi, who's frozen yoghurt gets the most vote win the game(for more details tell people please check Zelmi Chatterly). The total prize is up to $2,500, and they will also get a chance to win an tabvue2 with custom Zelmi vinyl cover.
We would like to see designs that use the colors black, white and pink. The final design should focus on attract school students, teenagers, college girls, and encourage them to come join the game with their friends.
school students, teenagers, college girls
competition starts on 19th July 2013, and ends 30th Oct. 2013
@ZELMI FROZEN YOGHURT MARLOW ARCADE EAST ( next to Brantly's)
College

```html
<!DOCTYPE html>
<html lang="en">
<head>
<meta charset="utf-8">
<title>Top Zelmi – Zelmi Frozen Yoghurt</title>
<link rel="stylesheet" href="https://fonts.googleapis.com/css2?family=Tinos:wght@400;700&family=Marcellus&family=Arimo&display=swap">
<style>
  :root {
    --pink: #e328f5;
    --white: #ffffff;
    --black: #000000;
    --lime: #33ff33;
    --placeholder-top: #b8f7a8;
    --placeholder-bottom: #f4e8f7;
  }
  html, body {
    margin: 0;
    padding: 0;
    overflow: hidden;
    background: var(--white);
  }
  .flyer {
    position: relative;
    width: 927px;
    height: 1200px;
    overflow: hidden;
    background: var(--pink);
    font-family: "Tinos", "Times New Roman", serif;
    color: var(--white);
  }
  .scallops {
    position: absolute;
    inset: 0;
  }
  .brand {
    position: absolute;
    top: 40px;
    left: 0;
    width: 100%;
    text-align: center;
  }
  .brand-name {
    display: block;
    color: var(--black);
    font-size: 120px;
    line-height: 1;
    letter-spacing: 14px;
  }
  .brand-sub {
    display: block;
    margin-top: 40px;
    color: var(--white);
    font-family: "Arimo", Arial, sans-serif;
    font-size: 21px;
    letter-spacing: 3px;
  }
  .presents {
    position: absolute;
    top: 264px;
    left: 0;
    width: 100%;
    margin: 0;
    text-align: center;
    color: var(--black);
    font-size: 27px;
  }
  .title {
    position: absolute;
    top: 298px;
    left: 168px;
    width: 592px;
    height: 140px;
  }
  .title text {
    font-family: "Marcellus", "Lucida Bright", serif;
    font-size: 84px;
    fill: var(--black);
    letter-spacing: 2px;
  }
  .treat-placeholder {
    position: absolute;
    left: 383px;
    top: 402px;
    width: 162px;
    height: 204px;
    background: linear-gradient(to bottom, var(--placeholder-top), var(--placeholder-bottom));
  }
  .copy {
    position: absolute;
    left: 0;
    width: 100%;
    margin: 0;
    text-align: center;
    font-size: 27px;
    line-height: 1.24;
  }
  .label {
    color: var(--black);
    font-weight: 700;
  }
  .hashtag {
    color: var(--lime);
    font-weight: 700;
  }
  .rules { top: 646px; }
  .prizes { top: 787px; left: -10px; }
  .more-info {
    top: 902px;
    font-size: 21px;
    color: var(--black);
  }
  .more-info .handle { color: var(--white); }
  .dates { top: 1064px; }
  .location { top: 1116px; }
</style>
</head>
<body>
<main class="flyer">
  <svg class="scallops" width="927" height="1200" viewBox="0 0 927 1200" aria-hidden="true">
    <g fill="#ffffff">
      <circle cx="-8" cy="18" r="72"/>
      <circle cx="-8" cy="168" r="72"/>
      <circle cx="-8" cy="318" r="72"/>
      <circle cx="-8" cy="468" r="72"/>
      <circle cx="-8" cy="618" r="72"/>
      <circle cx="-8" cy="768" r="72"/>
      <circle cx="-8" cy="918" r="72"/>
      <circle cx="-8" cy="1068" r="72"/>
      <circle cx="-8" cy="1218" r="72"/>
      <circle cx="935" cy="18" r="72"/>
      <circle cx="935" cy="168" r="72"/>
      <circle cx="935" cy="318" r="72"/>
      <circle cx="935" cy="468" r="72"/>
      <circle cx="935" cy="618" r="72"/>
      <circle cx="935" cy="768" r="72"/>
      <circle cx="935" cy="918" r="72"/>
      <circle cx="935" cy="1068" r="72"/>
      <circle cx="935" cy="1218" r="72"/>
    </g>
  </svg>

  <header class="brand">
    <span class="brand-name">ZELMI</span>
    <span class="brand-sub">FROZEN YOGHURT</span>
  </header>

  <p class="presents">Presents:</p>

  <svg class="title" viewBox="0 0 592 140" aria-label="Top Zelmi!">
    <defs>
      <path id="title-arc" d="M 10 132 Q 296 10 582 132"/>
    </defs>
    <text text-anchor="middle"><textPath href="#title-arc" startOffset="50%">Top Zelmi!</textPath></text>
  </svg>

  <div class="treat-placeholder" role="img" aria-label="Illustration area: a cup of green frozen yoghurt"></div>

  <p class="copy rules">
    <span class="label">Contest Rules:</span> Simply post your yoghurt creation<br>
    on Zelmi Chatterly and tag <span class="hashtag">#TOPZELMI</span><br>
    The frozen yoghurt with the most votes wins!
  </p>

  <p class="copy prizes">
    <span class="label">Prizes:</span> Up to $2,500 and the chance to<br>
    win an Tabvue2 with custom Zelmi vinyl cover!
  </p>

  <p class="copy more-info">
    For More Information Check out our Chatterly Page <span class="handle">@ZELMI FROZEN YOGHURT</span>
  </p>

  <p class="copy dates">Competition begins on 19th July 2013, and ends 30th Oct. 2013</p>

  <p class="copy location">Located @Marlow Arcade East,VIC, Australia. (Next to Brantly's)</p>
</main>
</body>
</html>
```